Real Estate Business card design

Company Name: Tamarind Holdings, LLC
subtitle: We pay cash for houses!
Daniel Whitcombe
Managing Director
555-214-0963
Dan@TamarindHoldingsLLC.example
www.TamarindHoldingsLLC.example

We pay referral fees for Seller and Buyer leads.

Back:
We offer referral fees for Seller and Buyer leads that close.

Please contact Hal at 555-214-0963 with your referrals or to learn more about the referral program!

I am open to different color options but I am going for a classic, elegant, clean, and professional look. Please use logo as a reference.

Target Market(s)

People selling their homes and people in the market for buying homes.

Contact Information for Business Card

please see project description

Font styles to use
Serif
Sans Serif
Script

Requirements
Must have
• must have my logo in it
Nice to have
• I like cards that are split down the middle but please come up with a few mock ups. Open to any color scheme.

```html
<!DOCTYPE html>
<html lang="en">
<head>
<meta charset="utf-8">
<title>Tamarind Holdings, LLC – Business Card</title>
<link rel="stylesheet" href="https://fonts.googleapis.com/css2?family=Montserrat:wght@300;400;500;600;700&family=Open+Sans:ital,wght@1,600&display=swap">
<style>
  :root {
    --slate: #424b57;
    --tan: #c0a07f;
    --paper: #f1f1f1;
    --ink: #1d1f22;
    --white: #ffffff;
    --backdrop: #e6e1d9;
  }
  * { margin: 0; padding: 0; box-sizing: border-box; }
  html, body { width: 900px; height: 1200px; overflow: hidden; }
  body {
    background: var(--backdrop);
    font-family: "Montserrat", sans-serif;
    position: relative;
  }
  .card {
    position: absolute;
    width: 774px;
    height: 448px;
    border-radius: 22px;
    overflow: hidden;
    box-shadow: 0 6px 18px rgba(0,0,0,0.18);
  }
  .card-front { left: 72px; top: 135px; background: var(--paper); }
  .card-back { left: 73px; top: 625px; background: var(--slate); color: var(--white); }

  .front-shapes { position: absolute; inset: 0; }

  .brand-mark {
    position: absolute;
    left: 40px; top: 130px;
    width: 310px;
    display: flex; align-items: center; gap: 12px;
    color: var(--white);
    font-weight: 600;
    font-size: 25px;
    line-height: 1.15;
  }
  .brand-mark .dot {
    flex: 0 0 18px; height: 18px; background: var(--tan);
  }

  .front-tagline {
    position: absolute;
    left: 38px; top: 352px;
    color: var(--white);
  }
  .front-tagline .company { font-size: 19px; font-weight: 400; }
  .front-tagline .slogan {
    font-family: "Open Sans", sans-serif;
    font-style: italic; font-weight: 600;
    font-size: 21px; margin-top: 4px;
  }

  .person {
    position: absolute; right: 30px; top: 46px;
    text-align: right; line-height: 1;
    font-size: 43px; letter-spacing: 3px;
  }
  .person .first { color: var(--slate); font-weight: 400; }
  .person .last { color: var(--tan); font-weight: 700; margin-top: 6px; }

  .contact-list {
    position: absolute; right: 33px; top: 202px;
    width: 357px; list-style: none;
    text-align: right; color: var(--ink);
    font-size: 17.5px;
  }
  .contact-list li { padding: 6px 0 7px; }
  .contact-list li + li { border-top: 1.5px solid var(--tan); }

  .referral-note {
    position: absolute; right: 33px; top: 357px;
    text-align: right; font-size: 18px; line-height: 1.45; color: var(--ink);
  }

  .back-lead {
    position: absolute; top: 40px; left: 0; right: 0;
    text-align: center; font-size: 18.5px; letter-spacing: 1.4px;
  }
  .back-brand {
    position: absolute; top: 190px; left: 0; right: 0;
    display: flex; justify-content: center; align-items: center; gap: 16px;
    font-weight: 600; font-size: 42px; color: var(--white);
  }
  .back-brand .dot { width: 22px; height: 22px; background: var(--tan); }
  .back-contact {
    position: absolute; top: 366px; left: 0; right: 0;
    text-align: center; font-size: 20.5px; letter-spacing: 1.6px; line-height: 1.4;
  }
  .back-contact strong { color: var(--tan); font-weight: 700; }
</style>
</head>
<body>

<section class="card card-front" aria-label="Business card front">
  <svg class="front-shapes" width="774" height="448" viewBox="0 0 774 448" aria-hidden="true">
    <polygon points="0,0 443,0 313,448 0,448" fill="var(--tan)"/>
    <polygon points="0,0 432,0 345,302 0,265" fill="var(--slate)"/>
    <polygon points="0,265 345,302 302,448 0,448" fill="var(--tan)"/>
  </svg>

  <div class="brand-mark"><span class="dot"></span><span>Tamarind Holdings, LLC</span></div>

  <div class="front-tagline">
    <p class="company">Tamarind Holdings, LLC</p>
    <p class="slogan">We pay cash for houses!</p>
  </div>

  <h1 class="person">
    <span class="first">DANIEL</span><br>
    <span class="last">WHITCOMBE</span>
  </h1>

  <ul class="contact-list">
    <li>555-214-0963</li>
    <li>Dan@TamarindHoldingsLLC.example</li>
    <li>www.TamarindHoldingsLLC.example</li>
  </ul>

  <p class="referral-note">We pay referral fees for<br>Seller and Buyer leads</p>
</section>

<section class="card card-back" aria-label="Business card back">
  <p class="back-lead">We offer referral fees for Seller and Buyer leads that close.</p>
  <div class="back-brand"><span class="dot"></span><span>Tamarind Holdings, LLC</span></div>
  <p class="back-contact"><strong>Please contact Hal at 555-214-0963</strong> with your<br>referrals or to learn more about the referral program!</p>
</section>

</body>
</html>
```